Popup Nightclub Grand Opening Flyer

We need to design a flyer for the grand opening of an upscale, exclusive nightclub called "Lanternfall". The design needs to be chic and exclusive. The background should be black and the text should primarily be white. We like minimalist designs.

Here is the text for the flyer
-
Velvetrope Atlanta Presents

Lanternfall (LOGO)

A Popup Nightclub Experience
For one night Only

Friday, October 18, 2013
Party begins at 9PM

INVITE ONLY

See invitation for location details
(Velvetrope Atlanta logo)

-
Examples we like

http://cdn2-b.brivelpost.com/sites/default/files/styles/image_content_width/hash/3d/fa/1472093815_4471_flyer.jpg?itok=R8kqWm2z

http://api.plovra.com/files/7Kqq-Tr82XXB3pQzJvmtR5HL2W719E4nbRtC6KLd4HsfM8Y2qTDK-VmjwDoNqLX4QBzTHD9nakRbVx3m-Pfq8htc3MDTWr5p4/2zelSaturdays.jpg

http://quenmar.com/wp-content/uploads/yootheme/widgetkit/gallery/2zel/2zel-gen_vroom4-01.jpg

Hi All, one thing that we are seeing that we don't like is on over emphasis on the phrase "a popup nightclub experience" please don't make this the largest thing on the flyer

Target Market(s)

Target market is 25-35 year olds who are affluent (rich) and like luxury brands

Requirements
Must have
• Dark Background
Nice to have
• Velvetrope Logo on the bottom
Modern text that isn't curvy
Should not have
• Curved text

```html
<!DOCTYPE html>
<html lang="en">
<head>
<meta charset="utf-8">
<title>Lanternfall Popup Nightclub Flyer</title>
<link rel="stylesheet" href="https://fonts.googleapis.com/css2?family=Josefin+Sans:wght@100;300&family=Montserrat:wght@300;400;500&display=swap">
<style>
  :root {
    --ink: #000000;
    --paper: #ffffff;
    --smoke: #2a2a2a;
    --ash: #5c5c5c;
    --haze: #cfcfcf;
    --soft: rgba(255,255,255,0.85);
  }
  * { margin: 0; padding: 0; box-sizing: border-box; }
  html, body {
    width: 927px; height: 1200px; overflow: hidden; background: var(--ink);
  }
  .flyer {
    position: relative; width: 927px; height: 1200px; overflow: hidden;
    background: var(--ink); color: var(--paper);
    font-family: "Montserrat", Arial, sans-serif;
  }
  .stage-lighting {
    position: absolute; left: 0; top: 0; width: 927px; height: 1065px;
    background:
      radial-gradient(ellipse 260px 190px at 463px 420px, rgba(255,255,255,0.55), rgba(255,255,255,0) 100%),
      radial-gradient(ellipse 340px 300px at 440px 820px, rgba(220,220,220,0.55), rgba(220,220,220,0) 100%),
      linear-gradient(180deg, #1b1b1b 0%, #2b2b2b 45%, #1e1e1e 100%);
  }
  .headline {
    position: absolute; left: 0; width: 100%; text-align: center;
    font-family: "Josefin Sans", Arial, sans-serif; font-weight: 100;
  }
  .headline--host { top: 18px; font-size: 70px; letter-spacing: 1px; }
  .headline--presents { top: 162px; font-size: 58px; }
  .venue-mark {
    position: absolute; left: 433px; top: 330px; width: 60px; height: 60px;
    border-radius: 50%; border: 4px solid var(--haze);
  }
  .venue-name {
    position: absolute; left: 0; width: 100%; top: 440px; text-align: center;
    font-weight: 300; font-size: 60px; letter-spacing: 8px; line-height: 1;
  }
  .venue-type {
    position: absolute; left: 0; width: 100%; top: 522px; text-align: center;
    font-weight: 300; font-size: 32px; letter-spacing: 6px; line-height: 1;
  }
  .tagline {
    position: absolute; left: 0; width: 100%; top: 565px; text-align: center;
    font-weight: 400; font-size: 28px; line-height: 30px;
  }
  .one-night {
    position: absolute; left: 297px; top: 642px; width: 339px; height: 34px;
    border-top: 2px solid var(--paper); border-bottom: 2px solid var(--paper);
    text-align: center; font-size: 24px; letter-spacing: 4px; line-height: 30px;
  }
  .details {
    position: absolute; right: 18px; top: 858px; text-align: right;
    font-size: 14.5px; letter-spacing: 3px; line-height: 20px; color: var(--soft);
    text-transform: uppercase;
  }
  .details p + p { margin-top: 24px; }
  .host-band {
    position: absolute; left: 0; top: 1065px; width: 927px; height: 135px;
    background: var(--ink);
  }
  .host-band__mark {
    position: absolute; left: 110px; top: 28px; width: 80px; height: 80px;
    border-radius: 50%; border: 4px solid var(--paper);
  }
  .host-band__divider {
    position: absolute; left: 290px; top: 11px; width: 2px; height: 98px; background: var(--paper);
  }
  .host-band__name {
    position: absolute; left: 326px; top: 10px; font-weight: 400;
    font-size: 76px; letter-spacing: 3px; line-height: 1;
  }
  .host-band__city {
    position: absolute; left: 328px; top: 84px; font-weight: 500;
    font-size: 30px; letter-spacing: 9px; line-height: 1;
  }
</style>
</head>
<body>
<main class="flyer">
  <div class="stage-lighting" role="img" aria-label="Dark grungy texture with a fan of white spotlight beams rising beneath the venue name"></div>

  <h1 class="headline headline--host">VELVETROPE ATLANTA</h1>
  <p class="headline headline--presents">PRESENTS</p>

  <div class="venue-mark"></div>
  <h2 class="venue-name">LANTERNFALL</h2>
  <p class="venue-type">NIGHTCLUB</p>
  <p class="tagline">A POPUP NIGHTCLUB<br>EXPERIENCE</p>
  <p class="one-night">ONE NIGHT ONLY</p>

  <div class="details">
    <p>Friday, October 18, 2013<br>Party begins at 9PM</p>
    <p>Invite only</p>
    <p>See invitation for location details</p>
  </div>

  <footer class="host-band">
    <div class="host-band__mark"></div>
    <div class="host-band__divider"></div>
    <p class="host-band__name">VELVETROPE</p>
    <p class="host-band__city">ATLANTA</p>
  </footer>
</main>
</body>
</html>
```